依頼詳細
キャンプ場の詳細ホームページがなく、今回新規でホームページを作ることとなりました。
雄大な自然の広がるキャンプ場です。非日常を体験してもらいたいたいです。
川の流れ、きじ、サギ、川鵜、トビ、カッコウ、鴨、ひばり、うぐいすなどの鳥、たぬき、きつね、いたち、いのししの動物も生息しています。

癒やされ、行ってみたくなるようなデザインをお願いします。
サイトURL
http://www.kawabe-leisure-garden.co.jp/resort.html
ページ数
1ページ
希望イメージ
シンプル 複雑
単色 カラフル
暗い 明るい
日常 高級
遊び心 厳粛
未来的 伝統的
女性的 男性的
希望する色
茶系、緑系、アースカラー
納品ファイル
• 高解像度JPG (.jpg)
• イラストレーター形式 (.ai)
• フォトショップ形式 (.psd)
補足説明
レスポンシブデザインを中心にご提案をお願いいたします。
イメージ写真 https://files.example-share.jp/open?id=7kQm2XpR9vTnWcz4Hs81LdEaYb3FuJo5&authuser=hiroaki@orangeleaf.co.jp

イメージ写真等は、有料素材写真等から選定して頂きご提案いただけると大変助かります。

添付写真は必ず使用してほしいものではありません。

```html
<!DOCTYPE html>
<html lang="ja">
<head>
<meta charset="utf-8">
<title>かわべレジャーガーデン | キャンプ場</title>
<link href="https://fonts.googleapis.com/css2?family=Noto+Sans+JP:wght@400;500;700&family=Noto+Serif+JP:wght@500;700&display=swap" rel="stylesheet">
<style>
:root{
  --green:#86ad3a;
  --green-dark:#5f8a22;
  --lime:#d5dd93;
  --brown:#8d6e5c;
  --brown-dark:#4a2f1e;
  --taupe:#d9cec9;
  --text:#555;
  --title:#4a3a2e;
  --line:#cbb9a8;
  --white:#fff;
}
*{box-sizing:border-box;margin:0;padding:0}
html,body{width:1200px;height:4176px;overflow:hidden}
body{font-family:"Noto Sans JP",sans-serif;color:var(--text);background:var(--white);position:relative;font-size:13px;line-height:1.9}
section,header,footer{position:absolute;left:0;width:1200px}
.dummy{font-size:11px;line-height:1.9;color:#777}

/* header */
.site-header{top:0;height:108px;background:var(--white)}
.brand{position:absolute;left:52px;top:14px;display:flex;align-items:center;gap:8px;font-weight:700;font-size:16px;color:var(--green-dark)}
.brand-mark{width:14px;height:14px;background:var(--green);border-radius:50%}
.contact{position:absolute;right:52px;top:14px;display:flex;align-items:center;gap:20px}
.tel{text-align:right;line-height:1.2;color:var(--title)}
.tel small{font-size:10px;display:block}
.tel strong{font-size:24px;letter-spacing:1px}
.btn-contact{background:var(--green);color:#fff;font-size:13px;padding:8px 22px;border-radius:3px}
.global-nav{position:absolute;left:200px;top:64px;display:flex;gap:0}
.global-nav a{font-size:13px;color:var(--title);text-decoration:none;padding:10px 20px;border-left:1px solid #ddd}
.global-nav a:first-child{border-left:none}

/* hero */
.hero{top:108px;height:512px;background:linear-gradient(180deg,#9fc4d9 0%,#8fae6a 35%,#4e6e2c 70%,#7fa43c 100%)}
.hero-copy{position:absolute;left:360px;top:172px;font-family:"Noto Serif JP",serif;color:#fff;font-size:30px;line-height:1.7;text-shadow:0 2px 6px rgba(0,0,0,.45);font-weight:500}
.hero-copy em{font-style:normal;color:#ffe7a0;font-size:38px}

/* section title */
.sec-title{text-align:center;font-size:22px;font-weight:700;color:var(--title);display:flex;justify-content:center;align-items:center;gap:12px}
.sec-title svg{width:14px;height:22px}
.sec-title .accent{color:var(--green)}

/* kodawari */
.kodawari{top:620px;height:332px}
.kodawari .sec-title{margin-top:34px;font-size:26px}
.circle{position:absolute;top:100px;width:220px;height:200px;border-radius:50%}
.circle.left{left:40px;background:linear-gradient(135deg,#8aa35a,#d9cdb5 55%,#6d8a3e)}
.circle.right{right:40px;background:linear-gradient(135deg,#6f9a45,#9ab9c7 50%,#5b7f30)}
.kodawari-text{position:absolute;left:300px;width:600px;top:110px;text-align:center}

/* facility */
.facility{top:952px;height:560px;background:var(--lime)}
.facility .sec-title{margin-top:66px}
.facility-photo{position:absolute;left:220px;top:128px;width:360px;height:252px;background:linear-gradient(160deg,#6d8b47,#a9b67c 50%,#597a30)}
.facility-text{position:absolute;left:612px;top:128px;width:370px}
.btn{position:absolute;left:50%;transform:translateX(-50%);width:344px;height:52px;border-radius:4px;display:flex;align-items:center;justify-content:center;font-size:14px;color:#fff;background:var(--brown);letter-spacing:1px}
.btn.light{background:#fff;color:var(--title);box-shadow:0 1px 3px rgba(0,0,0,.12)}
.facility .btn{top:476px}

/* flow */
.flow{top:1512px;height:520px}
.flow .sec-title{margin-top:56px}
.flow-text{position:absolute;left:228px;top:112px;width:350px}
.flow-steps{position:absolute;left:650px;top:118px;width:270px}
.step{border:1px solid var(--green);height:40px;display:flex;align-items:center;justify-content:center;font-size:12px;color:var(--title);background:#fff}
.step-arrow{display:block;margin:3px auto;width:14px;height:8px}
.flow .btn{top:450px}

/* map */
.map{top:2056px;height:304px;background:linear-gradient(120deg,#e9ece4 0%,#dfe6d6 40%,#cfdfe9 60%,#e8ebe2 100%)}
.map-card{position:absolute;left:12px;top:14px;width:190px;height:58px;background:#fff;box-shadow:0 1px 4px rgba(0,0,0,.2);font-size:9px;padding:6px 8px;line-height:1.5}
.map-pin{position:absolute;left:560px;top:120px;width:22px;height:32px}

/* access */
.access{top:2360px;height:320px}
.access-box{position:absolute;left:228px;top:40px;width:320px;border:1px solid var(--line);border-radius:3px;padding:14px 18px}
.access-box h3{font-size:12px;color:var(--title);font-weight:700;margin-top:6px}
.access-box h3:first-child{margin-top:0}
.access-box p{font-size:11px;line-height:1.6}
.access-text{position:absolute;left:600px;top:40px;width:380px}

/* voices */
.voices{top:2700px;height:480px;background:var(--taupe)}
.voices .sec-title{margin-top:110px}
.voice-list{position:absolute;left:236px;top:176px;display:flex;gap:34px}
.voice{width:218px;height:278px;background:#fff;padding:8px}
.voice-photo{height:116px}
.voice:nth-child(1) .voice-photo{background:linear-gradient(135deg,#8c6a4c,#b9a07e,#6a5a3a)}
.voice:nth-child(2) .voice-photo{background:linear-gradient(135deg,#6b6a52,#a59678,#4f4a38)}
.voice:nth-child(3) .voice-photo{background:linear-gradient(135deg,#6c8c4e,#9fb6a4,#4f6c34)}
.voice p{margin-top:10px}

/* faq */
.faq{top:3190px;height:540px}
.faq .sec-title{margin-top:64px}
.faq-list{position:absolute;left:228px;top:120px;width:744px}
.faq-item{border:1px solid var(--line);border-radius:3px;margin-bottom:16px;background:#fff}
.faq-q{display:flex;align-items:center;height:46px;padding:0 18px;font-size:13px;color:var(--title);gap:14px}
.faq-q .mark{color:var(--green);font-weight:700;font-size:18px}
.faq-q .toggle{margin-left:auto;font-size:18px;color:#444}
.faq-a{display:flex;gap:14px;padding:4px 18px 18px}
.faq-a .mark{color:var(--brown);font-weight:700;font-size:18px}

/* recruit */
.recruit{top:3740px;height:290px;background:linear-gradient(90deg,#f7f5f2 0%,#f3f0ec 45%,#e9e2d9 70%,#d9cbbb 100%)}
.recruit-photo{position:absolute;right:0;top:0;width:520px;height:290px;background:linear-gradient(90deg,rgba(243,240,236,0),#d6c6b3 60%,#c7b39c)}
.recruit .sec-title{margin-top:30px}
.recruit-text{position:absolute;left:228px;top:86px;width:380px}
.recruit .btn{left:228px;transform:none;top:224px}

/* footer */
.site-footer{top:4030px;height:146px;background:var(--brown-dark);color:#fff;text-align:center}
.footer-nav{display:flex;justify-content:center;gap:30px;margin-top:24px;font-size:11px}
.footer-tel{display:inline-block;margin-top:16px;border:1px solid rgba(255,255,255,.7);padding:4px 26px;line-height:1.3}
.footer-tel small{font-size:9px;display:block}
.footer-tel strong{font-size:20px}
.copyright{font-size:9px;margin-top:12px;opacity:.75}
</style>
</head>
<body>

<header class="site-header">
  <div class="brand"><span class="brand-mark"></span>かわべレジャーガーデン</div>
  <div class="contact">
    <div class="tel"><small>お電話でのお問い合わせ</small><strong>0120-000-0000</strong></div>
    <div class="btn-contact">お問い合わせ</div>
  </div>
  <nav class="global-nav">
    <a>HOME</a><a>施設紹介</a><a>予約の流れ</a><a>よくある質問</a><a>お客様の声</a><a>アクセス</a><a>会社概要</a><a>お問い合わせ</a>
  </nav>
</header>

<section class="hero" role="img" aria-label="森に囲まれた芝生広場と三角屋根のロッジの写真">
  <p class="hero-copy">雄大な<em>自然</em>と動植物<br>非日常の空間を体験</p>
</section>

<section class="kodawari">
  <h2 class="sec-title">かわべリゾートの<span class="accent">こだわり</span></h2>
  <div class="circle left" role="img" aria-label="草原に張られた大型テントの写真"></div>
  <div class="circle right" role="img" aria-label="川辺の緑豊かな湿地の写真"></div>
  <p class="kodawari-text dummy">ここにテキストが入ります。ここにテキストが入ります。ここにテキストが入ります。<br>ここにテキストが入ります。ここにテキストが入ります。ここにテキストが入ります。<br>ここにテキストが入ります。ここにテキストが入ります。ここにテキストが入ります。<br>ここにテキストが入ります。ここにテキストが入ります。<br><br>ここにテキストが入ります。ここにテキストが入ります。ここにテキストが入ります。<br>ここにテキストが入ります。ここにテキストが入ります。</p>
</section>

<section class="facility">
  <h2 class="sec-title"><svg viewBox="0 0 14 22"><path d="M7 0L13 11L7 22L1 11Z" fill="#86ad3a"/></svg>施設紹介<svg viewBox="0 0 14 22"><path d="M7 0L13 11L7 22L1 11Z" fill="#86ad3a"/></svg></h2>
  <div class="facility-photo" role="img" aria-label="キャンプ場全体を上空から見た写真"></div>
  <p class="facility-text dummy">ここにテキストが入ります。ここにテキストが入ります。ここにテキストが入ります。ここにテキストが入ります。ここにテキストが入ります。ここにテキストが入ります。ここにテキストが入ります。ここにテキストが入ります。ここにテキストが入ります。<br><br>ここにテキストが入ります。ここにテキストが入ります。ここにテキストが入ります。ここにテキストが入ります。ここにテキストが入ります。ここにテキストが入ります。</p>
  <div class="btn light">詳しくはこちら</div>
</section>

<section class="flow">
  <h2 class="sec-title"><svg viewBox="0 0 14 22"><path d="M7 0L13 11L7 22L1 11Z" fill="#86ad3a"/></svg>予約の流れ<svg viewBox="0 0 14 22"><path d="M7 0L13 11L7 22L1 11Z" fill="#86ad3a"/></svg></h2>
  <p class="flow-text dummy">ここにテキストが入ります。ここにテキストが入ります。ここにテキストが入ります。ここにテキストが入ります。ここにテキストが入ります。ここにテキストが入ります。<br><br>ここにテキストが入ります。ここにテキストが入ります。ここにテキストが入ります。ここにテキストが入ります。ここにテキストが入ります。<br><br>ここにテキストが入ります。ここにテキストが入ります。ここにテキストが入ります。ここにテキストが入ります。</p>
  <div class="flow-steps">
    <div class="step">ご予約の流れが入ります。</div>
    <svg class="step-arrow" viewBox="0 0 14 8"><path d="M0 0H14L7 8Z" fill="#86ad3a"/></svg>
    <div class="step">ご予約の流れが入ります。</div>
    <svg class="step-arrow" viewBox="0 0 14 8"><path d="M0 0H14L7 8Z" fill="#86ad3a"/></svg>
    <div class="step">ご予約の流れが入ります。</div>
    <svg class="step-arrow" viewBox="0 0 14 8"><path d="M0 0H14L7 8Z" fill="#86ad3a"/></svg>
    <div class="step">ご予約の流れが入ります。</div>
    <svg class="step-arrow" viewBox="0 0 14 8"><path d="M0 0H14L7 8Z" fill="#86ad3a"/></svg>
    <div class="step">ご予約の流れが入ります。</div>
  </div>
  <div class="btn">詳しくはこちら</div>
</section>

<section class="map" role="img" aria-label="キャンプ場周辺の川と道路の地図">
  <div class="map-card">かわべレジャーガーデン<br>〇〇県〇〇市〇〇町0-0-0</div>
  <svg class="map-pin" viewBox="0 0 22 32"><path d="M11 0C5 0 0 5 0 11c0 8 11 21 11 21s11-13 11-21C22 5 17 0 11 0z" fill="#d9443a"/><circle cx="11" cy="11" r="4" fill="#fff"/></svg>
</section>

<section class="access">
  <div class="access-box">
    <h3>お車でお越しの方</h3><p>〇〇〇〇から約〇〇分<br>〇〇〇〇から約〇〇分</p>
    <h3>バスでお越しの方</h3><p>〇〇〇〇から約〇〇分<br>〇〇〇〇から約〇〇分</p>
    <h3>電車でお越しの方</h3><p>〇〇〇〇から約〇〇分<br>〇〇〇〇から約〇〇分</p>
  </div>
  <p class="access-text dummy">ここにテキストが入ります。ここにテキストが入ります。ここにテキストが入ります。ここにテキストが入ります。<br><br>ここにテキストが入ります。ここにテキストが入ります。ここにテキストが入ります。ここにテキストが入ります。<br><br>ここにテキストが入ります。ここにテキストが入ります。ここにテキストが入ります。</p>
</section>

<section class="voices">
  <h2 class="sec-title"><svg viewBox="0 0 14 22"><path d="M7 0L13 11L7 22L1 11Z" fill="#86ad3a"/></svg>お客様の声<svg viewBox="0 0 14 22"><path d="M7 0L13 11L7 22L1 11Z" fill="#86ad3a"/></svg></h2>
  <div class="voice-list">
    <div class="voice"><div class="voice-photo" role="img" aria-label="焚き火を囲むキャンプの写真"></div><p class="dummy">ここにテキストが入ります。ここにテキストが入ります。ここにテキストが入ります。ここにテキストが入ります。ここにテキストが入ります。</p></div>
    <div class="voice"><div class="voice-photo" role="img" aria-label="バーベキューの料理の写真"></div><p class="dummy">ここにテキストが入ります。ここにテキストが入ります。ここにテキストが入ります。ここにテキストが入ります。ここにテキストが入ります。</p></div>
    <div class="voice"><div class="voice-photo" role="img" aria-label="林の中に並ぶテントの写真"></div><p class="dummy">ここにテキストが入ります。ここにテキストが入ります。ここにテキストが入ります。ここにテキストが入ります。ここにテキストが入ります。</p></div>
  </div>
</section>

<section class="faq">
  <h2 class="sec-title"><svg viewBox="0 0 14 22"><path d="M7 0L13 11L7 22L1 11Z" fill="#86ad3a"/></svg>よくある質問<svg viewBox="0 0 14 22"><path d="M7 0L13 11L7 22L1 11Z" fill="#86ad3a"/></svg></h2>
  <div class="faq-list">
    <div class="faq-item">
      <div class="faq-q"><span class="mark">Q</span>質問内容が入ります。<span class="toggle">×</span></div>
      <div class="faq-a"><span class="mark">A</span><p class="dummy">ここにテキストが入ります。ここにテキストが入ります。ここにテキストが入ります。ここにテキストが入ります。ここにテキストが入ります。ここにテキストが入ります。ここにテキストが入ります。ここにテキストが入ります。ここにテキストが入ります。</p></div>
    </div>
    <div class="faq-item"><div class="faq-q"><span class="mark">Q</span>質問内容が入ります。<span class="toggle">+</span></div></div>
    <div class="faq-item"><div class="faq-q"><span class="mark">Q</span>質問内容が入ります。<span class="toggle">+</span></div></div>
  </div>
</section>

<section class="recruit">
  <div class="recruit-photo" role="img" aria-label="ノートに書き込む手元の写真"></div>
  <h2 class="sec-title"><svg viewBox="0 0 14 22"><path d="M7 0L13 11L7 22L1 11Z" fill="#86ad3a"/></svg>採用情報<svg viewBox="0 0 14 22"><path d="M7 0L13 11L7 22L1 11Z" fill="#86ad3a"/></svg></h2>
  <p class="recruit-text dummy">ここにテキストが入ります。ここにテキストが入ります。ここにテキストが入ります。ここにテキストが入ります。ここにテキストが入ります。ここにテキストが入ります。</p>
  <div class="btn">詳しくはこちら</div>
</section>

<footer class="site-footer">
  <nav class="footer-nav"><span>HOME</span><span>施設紹介</span><span>予約の流れ</span><span>よくある質問</span><span>お客様の声</span><span>アクセス</span><span>会社概要</span><span>お問い合わせ</span></nav>
  <div class="footer-tel"><small>お電話でのお問い合わせ</small><strong>0120-000-0000</strong></div>
  <p class="copyright">Copyright © かわべレジャーガーデン All Rights Reserved.</p>
</footer>

</body>
</html>
```